依頼詳細
PCとスマホデザインの両方納品をいただきますが、
まずはデザインイメージが確認しやすいPCページのみの提案をお願いします。
スマホページは当選者に納品時にお願いしたいと思います。
スマホサイズについて、表示は横幅375pxで作成し、
デザインデータは2倍の横幅750pxのカンバスサイズで作成してください。
(Retinaディスプレイに対応するため)
レスポンシブウェブデザインを意識したデザインでお願いします。

■サイトマップ
添付の画面遷移図をご確認ください。

■参考サイト
https://www.kurumi-p.co.jp/
https://www.m-sorano.co.jp/
https://www.fujino-printing.co.jp/

■内容について
印刷会社のサイトリニューアルになります。
既存サイト
https://www.hinata-printing.co.jp/

■素材写真
画像データについては、フリー素材から流用して
イメージ画像に当て込んでください。
足りない場合は、一旦他のサイトの写真をサンプルとして
入れてください。(サンプルなどの表記をお願いします)
また、購入が必要な写真などを利用した場合、
価格とサイト名を教えてください。

また、Pixmora Stockで定期契約をしていますので、
Pixmora Stockの画像は使用できます。
デザイン時はカンプ画像をお入れいただきますようお願いします。

※採用サイト寄りのサイトにしたいので、使用する画像は
なるべく人物が入っているものを使用してください。

■ワイヤーフレーム
https://mock.plavetta.jp/view/51830427-216b-4c73-9a05-87162534907e-4182/?fullscreen
コンテンツの構成としてワイヤーフレームを作成しましたが
必ずしもワイヤーフレームの通りではなくて大丈夫です。
TOPページに配置するコンテンツを見ていただき、デザインは
デザイナーの皆様におまかせしたいと思います。

----------------------------------------------------------------------------
【制作物に対するお願い】

■フォントについて
・無料で使えるフォントで作成をお願いします。
・OSに紐づくフォントの使用は控えていただければと思います (ヒラギノなど)

ページ数
1ページ
希望イメージ
シンプル 複雑
単色 カラフル
暗い 明るい
日常 高級
遊び心 厳粛
未来的 伝統的
女性的 男性的
希望する色
青系、既存サイトに載っているロゴのイメージでお願いします。
納品ファイル
• 高解像度JPG (.jpg)
• イラストレーター形式 (.ai)
• フォトショップ形式 (.psd)
補足説明
上記のいずれか1つ(アウトラインありとなしの2つ)と高解像度JPGを納品お願いします。
adobe XDでの納品も可能です。

```html
<!DOCTYPE html>
<html lang="ja">
<head>
<meta charset="utf-8">
<title>ヒナタ印刷 | お客様第一主義</title>
<link href="https://fonts.googleapis.com/css2?family=Noto+Serif+JP:wght@400;600;700&family=Noto+Sans+JP:wght@400;500;700&display=swap" rel="stylesheet">
<style>
:root{
  --blue:#1d8fd6;
  --blue-dark:#136aa3;
  --ink:#2b2f35;
  --text:#555a60;
  --muted:#8a8f95;
  --line:#d9dcdf;
  --paper:#ffffff;
  --soft:#f2f2f1;
  --band:#a9a9a9;
  --footer:#3a4651;
}
*{margin:0;padding:0;box-sizing:border-box}
html,body{width:1200px;height:4044px;overflow:hidden;background:var(--paper)}
body{position:relative;font-family:"Noto Serif JP",serif;color:var(--ink)}
.abs{position:absolute}
/* header */
.site-header{position:absolute;left:0;top:0;width:1200px;height:120px;background:var(--paper);z-index:2;box-shadow:0 2px 6px rgba(0,0,0,.08)}
.brand{position:absolute;left:104px;top:34px;display:flex;align-items:center;gap:14px}
.brand-mark{width:44px;height:44px;background:var(--blue)}
.brand-name{font-size:36px;font-weight:700;color:var(--blue-dark);letter-spacing:2px}
.global-nav{position:absolute;left:472px;top:0;height:120px;display:flex}
.global-nav a{display:flex;align-items:center;justify-content:center;width:146px;height:120px;font-family:"Noto Sans JP",sans-serif;font-size:15px;color:var(--ink);text-decoration:none}
.global-nav a.is-current{background:#4a5058;color:#fff}
.global-nav a.contact{background:var(--blue);color:#fff;width:144px}
/* hero */
.hero-photo{position:absolute;left:0;top:120px;width:1200px;height:1232px;background:linear-gradient(160deg,#5d6267 0%,#3a3e43 35%,#2c3034 60%,#4b4f58 80%,#6a5f6a 100%)}
.hero-title{position:absolute;top:318px;width:1200px;text-align:center;color:#fff;font-size:58px;font-weight:600;letter-spacing:6px}
.hero-sub{position:absolute;top:402px;width:1200px;text-align:center;color:#e8e8e8;font-size:20px;letter-spacing:4px}
.hero-lead{position:absolute;left:108px;top:680px;color:#fff;font-size:22px;line-height:1.9;letter-spacing:2px}
.hero-copy{position:absolute;left:640px;top:900px;width:460px;color:#f0f0f0;font-size:14px;line-height:2.1}
.hero-copy p+p{margin-top:26px}
/* business */
.business{position:absolute;left:0;top:1420px;width:1200px;height:460px;background:var(--soft)}
.section-title{font-size:18px;font-weight:600;letter-spacing:3px}
.business .section-title{position:absolute;top:120px;width:1200px;text-align:center}
.business .rule{position:absolute;left:580px;top:160px;width:40px;height:2px;background:var(--blue)}
.business-text{position:absolute;top:188px;width:1200px;text-align:center;font-size:14px;line-height:2;color:var(--text)}
.more{position:absolute;left:520px;top:324px;display:flex;align-items:center;gap:20px;font-size:15px;color:var(--ink)}
.arrow-dot{width:44px;height:44px;border-radius:50%;background:var(--blue);display:flex;align-items:center;justify-content:center}
/* cases */
.cases-head{position:absolute;left:108px;top:2050px}
.cases-head .rule{margin-top:10px;width:40px;height:2px;background:var(--blue)}
.pill{position:absolute;left:1010px;top:2050px;width:84px;height:40px;border-radius:20px;background:var(--blue);color:#fff;font-family:"Noto Sans JP",sans-serif;font-size:13px;display:flex;align-items:center;justify-content:center;gap:6px}
.cases-band{position:absolute;left:0;top:2260px;width:1200px;height:540px;background:var(--band)}
.case-card{position:absolute;top:2120px;width:316px;height:440px;background:#fff;box-shadow:0 4px 14px rgba(0,0,0,.15)}
.case-photo{height:240px}
.case-body{padding:24px 26px}
.case-title{font-size:15px;font-weight:600;letter-spacing:2px;margin-bottom:12px}
.case-text{font-size:13px;line-height:1.9;color:var(--text)}
/* banners */
.banner{position:absolute;top:2888px;width:476px;height:272px;display:flex;align-items:center;justify-content:center}
.banner-label{background:rgba(255,255,255,.9);padding:18px 44px;font-size:17px;letter-spacing:3px}
.banner.framed{outline:3px solid var(--blue);outline-offset:-12px}
/* news */
.news{position:absolute;top:3330px;width:472px}
.news .section-title{margin-bottom:12px}
.news .rule{height:2px;background:var(--blue)}
.news-item{display:flex;align-items:center;border-bottom:1px solid var(--line);height:64px}
.news-date{width:90px;font-size:12px;line-height:1.5;color:var(--muted);text-align:center}
.news-text{font-size:14px;color:var(--text);padding-left:20px}
.tag{font-family:"Noto Sans JP",sans-serif;font-size:12px;border:1px solid var(--line);padding:5px 12px;margin-left:20px;color:var(--text)}
/* footer */
.site-footer{position:absolute;left:0;top:3760px;width:1200px;height:284px;background:var(--footer);color:#fff}
.site-footer .brand{left:108px;top:54px}
.site-footer .brand-name{color:#fff}
.site-footer .brand-mark{background:#fff}
.foot-links{position:absolute;left:108px;top:150px;display:flex;gap:30px;font-family:"Noto Sans JP",sans-serif;font-size:12px;color:#c9d0d6}
.foot-info{position:absolute;left:780px;top:52px;font-family:"Noto Sans JP",sans-serif;font-size:13px;line-height:1.9;color:#dfe4e8}
.foot-tel{position:absolute;left:780px;top:130px;font-family:"Noto Sans JP",sans-serif;font-size:18px;line-height:1.7;font-weight:500}
.to-top{position:absolute;left:1036px;top:148px;width:56px;height:56px;background:var(--blue);display:flex;flex-direction:column;align-items:center;justify-content:center;font-family:"Noto Sans JP",sans-serif;font-size:10px;gap:2px}
.copyright{position:absolute;top:252px;width:1200px;text-align:center;font-family:"Noto Sans JP",sans-serif;font-size:11px;color:#aab3bb}
</style>
</head>
<body>

<header class="site-header">
  <div class="brand"><span class="brand-mark"></span><span class="brand-name">ヒナタ印刷</span></div>
  <nav class="global-nav">
    <a class="is-current">事業案内</a>
    <a>入稿について</a>
    <a>事例紹介</a>
    <a>会社概要</a>
    <a class="contact">お問い合わせ</a>
  </nav>
</header>

<section>
  <div class="hero-photo" role="img" aria-label="印刷機で刷り上がった用紙を扱う作業風景の写真"></div>
  <h1 class="hero-title">お客様第一主義</h1>
  <p class="hero-sub">お客様の発展が私たちの成長</p>
  <p class="hero-lead">ヒナタ印刷は<br>お客様と共に考えます。</p>
  <div class="hero-copy">
    <p>創業以来、地域の皆様に支えられながら、チラシやパンフレット、名刺から冊子まで幅広い印刷物をお届けしてまいりました。</p>
    <p>企画からデザイン、印刷、加工、発送まで一貫して対応し、お客様の想いを形にするお手伝いをいたします。</p>
    <p>これからもお客様と共に考え、共に成長できる会社であり続けるために、技術と品質の向上に努めてまいります。</p>
  </div>
</section>

<section class="business">
  <h2 class="section-title">事業案内</h2>
  <div class="rule"></div>
  <p class="business-text">ヒナタ印刷では企画から加工までお客様に合わせた<br>最適な印刷物をご提案いたします。<br>“伝えたい想いを形に”ご相談ください。</p>
  <div class="more">
    <span class="arrow-dot"><svg width="14" height="14" viewBox="0 0 14 14"><path d="M4 2l6 5-6 5" fill="none" stroke="#fff" stroke-width="2"/></svg></span>
    <span>詳しく見る</span>
  </div>
</section>

<section>
  <div class="cases-head"><h2 class="section-title">事例紹介</h2><div class="rule"></div></div>
  <div class="pill">一覧を見る<svg width="10" height="10" viewBox="0 0 10 10"><path d="M3 1l4 4-4 4" fill="none" stroke="#fff" stroke-width="1.6"/></svg></div>
  <div class="cases-band"></div>
  <article class="case-card" style="left:108px">
    <div class="case-photo" role="img" aria-label="開いたパンフレットの写真" style="background:linear-gradient(135deg,#e9e6e0,#c9c4bb)"></div>
    <div class="case-body"><h3 class="case-title">タイトルタイトルタイトル</h3><p class="case-text">テキストが入ります。テキストが入ります。テキストが入ります。テキストが入ります。</p></div>
  </article>
  <article class="case-card" style="left:442px">
    <div class="case-photo" role="img" aria-label="黒と金のパッケージ印刷の写真" style="background:linear-gradient(135deg,#2a2622,#6d5a3a)"></div>
    <div class="case-body"><h3 class="case-title">タイトルタイトルタイトル</h3><p class="case-text">テキストが入ります。テキストが入ります。テキストが入ります。テキストが入ります。</p></div>
  </article>
  <article class="case-card" style="left:776px">
    <div class="case-photo" role="img" aria-label="クラフト紙の箱とタグの写真" style="background:linear-gradient(135deg,#ece8e2,#b89b78)"></div>
    <div class="case-body"><h3 class="case-title">タイトルタイトルタイトル</h3><p class="case-text">テキストが入ります。テキストが入ります。テキストが入ります。テキストが入ります。</p></div>
  </article>
</section>

<section>
  <div class="banner" role="img" aria-label="印刷工場の写真" style="left:108px;background:linear-gradient(135deg,#4b4f55,#7a7d82)"><span class="banner-label">会社概要</span></div>
  <div class="banner framed" role="img" aria-label="積み重ねた印刷物の写真" style="left:616px;background:linear-gradient(135deg,#8b9096,#c4c6c9)"><span class="banner-label">入稿について</span></div>
</section>

<section>
  <div class="news" style="left:108px">
    <h2 class="section-title">新着情報</h2><div class="rule"></div>
    <div class="news-item"><span class="news-date">2021<br>12/07</span><span class="news-text">テキストが入ります。テキストが入ります。</span></div>
    <div class="news-item"><span class="news-date">2021<br>12/07</span><span class="news-text">テキストが入ります。テキストが入ります。</span></div>
    <div class="news-item"><span class="news-date">2021<br>12/07</span><span class="news-text">テキストが入ります。テキストが入ります。</span></div>
  </div>
  <div class="news" style="left:620px">
    <h2 class="section-title">ブログ</h2><div class="rule"></div>
    <div class="news-item"><span class="news-date">2022<br>01/12</span><span class="tag">新年のご挨拶</span></div>
    <div class="news-item"><span class="news-date">2022<br>01/05</span><span class="tag">加工機を導入しました</span></div>
    <div class="news-item"><span class="news-date">2021<br>12/27</span><span class="tag">年末年始のお知らせ</span></div>
  </div>
</section>

<footer class="site-footer">
  <div class="brand"><span class="brand-mark"></span><span class="brand-name">ヒナタ印刷</span></div>
  <div class="foot-links"><span>事業案内</span><span>入稿について</span><span>事例紹介</span><span>会社概要</span></div>
  <div class="foot-info">〒000-0000<br>みどり県あおば市中央町1丁目2番3号</div>
  <div class="foot-tel">TEL 012-345-6789<br>FAX 012-345-6790</div>
  <div class="to-top"><svg width="14" height="10" viewBox="0 0 14 10"><path d="M1 8l6-6 6 6" fill="none" stroke="#fff" stroke-width="2"/></svg>TOP</div>
  <p class="copyright">© HINATA PRINTING All Rights Reserved.</p>
</footer>

</body>
</html>
```